Einladung zum Geburtstag
Einladung zu einer Geburtstagsparty von zwei "Mädels", die zusammen 99 Jahre jung werden.
Eine wird 55 (25.8.) die andere 44. (24.8.) - alles "Schnapszahlen".
Es soll eine kleine Party tagsüber für die Arbeitskollegen werden, mit Imbiss und Umtrunk. Termin für die Feier ist der 25.8. ab 14h.
Die Einladung soll sowohl gedruckt als auch per Mail verschickt werden können.

```html
<!DOCTYPE html>
<html lang="de">
<head>
<meta charset="utf-8">
<title>Einladung – 44+55=99</title>
<link rel="stylesheet" href="https://fonts.googleapis.com/css2?family=Italianno&family=Great+Vibes&display=swap">
<style>
  :root {
    --ink: #0a0b0c;
    --gold: #b8955a;
    --gold-light: #f2e4bd;
    --gold-pale: #fbf3dc;
    --white: #ffffff;
  }
  html, body {
    margin: 0;
    padding: 0;
    overflow: hidden;
    background: var(--white);
  }
  .invitation {
    position: relative;
    width: 845px;
    height: 1200px;
    overflow: hidden;
    background: var(--white);
  }
  .invitation__frame {
    position: absolute;
    inset: 0;
  }
  .invitation__text {
    position: absolute;
    left: 0;
    width: 845px;
    margin: 0;
    text-align: center;
    white-space: nowrap;
    font-weight: 400;
  }
  .headline {
    top: 92px;
    font-family: "Great Vibes", cursive;
    font-size: 138px;
    line-height: 160px;
    color: var(--gold);
    letter-spacing: 1px;
  }
  .message {
    top: 258px;
    font-family: "Italianno", cursive;
    font-size: 82px;
    line-height: 88px;
    color: var(--white);
  }
  .message span { display: block; }
  .details {
    font-family: "Italianno", cursive;
    font-size: 52px;
    line-height: 60px;
  }
  .details--time { top: 815px; color: var(--gold); }
  .details--date { top: 880px; color: var(--white); }
  .sum {
    top: 950px;
    font-family: "Italianno", cursive;
    font-size: 150px;
    line-height: 150px;
    color: var(--gold);
    letter-spacing: 2px;
  }
</style>
</head>
<body>
<main class="invitation">
  <svg class="invitation__frame" width="845" height="1200" viewBox="0 0 845 1200" aria-hidden="true">
    <defs>
      <linearGradient id="frameGold" x1="0" y1="0" x2="1" y2="1">
        <stop offset="0" stop-color="#b8955a"/>
        <stop offset="0.3" stop-color="#f2e4bd"/>
        <stop offset="0.5" stop-color="#fbf3dc"/>
        <stop offset="0.7" stop-color="#e6d09c"/>
        <stop offset="1" stop-color="#b8955a"/>
      </linearGradient>
    </defs>
    <rect x="0" y="0" width="845" height="1200" fill="var(--ink)"/>
    <path fill="url(#frameGold)" fill-rule="evenodd"
      d="M60 12 L830 8 L838 60 L835 1130 L830 1190 L70 1192 L10 1185 L14 620 L18 40 Z
         M78 72 L772 64 L790 80 L786 1120 L772 1142 L90 1148 L76 1130 L80 600 Z"/>
    <path fill="none" stroke="var(--gold)" stroke-width="3"
      d="M78 72 L772 64 L790 80 L786 1120 L772 1142 L90 1148 L76 1130 L80 600 Z"/>
  </svg>

  <h1 class="invitation__text headline">Einladung</h1>

  <p class="invitation__text message">
    <span>Wir wollen feiern,</span>
    <span>den wir haben zusammen</span>
    <span>fast ein ganzen</span>
    <span>Jahrhundert geschafft.</span>
    <span>Wir freuen uns über jeden</span>
    <span>der mit uns feiern möchte..</span>
  </p>

  <p class="invitation__text details details--time">Uhrzeit:&nbsp; 14:00 Uhr</p>
  <p class="invitation__text details details--date">Wann: 25.08.2011</p>

  <p class="invitation__text sum">44+55=99</p>
</main>
</body>
</html>
```